K.T.L Electrical Services Pty Ltd

Electrical contracting business. I have a base for the design which i like. The contact number needs to be changed to 0491736250 and the O made more solid and level with the rest of the letters. If you have any other ideas of what would make it better I'm happy to see them.

The back side to be written as dot points with the following:
- Residential & Commercial
- Maintenance
- PV & Battery servicing
- EV Chargers

```html
<!DOCTYPE html>
<html lang="en">
<head>
<meta charset="utf-8">
<title>K.T.L Electrical Services – Business Card</title>
<link href="https://fonts.googleapis.com/css2?family=Poppins:wght@400;500&display=swap" rel="stylesheet">
<style>
  :root {
    --backdrop: #7f7d7e;
    --card-dark: #1f2a30;
    --teal: #8fb3b4;
    --teal-soft: #93b4b5;
    --white: #ffffff;
    --ink: #121212;
    --icon-fill: #e4e6e6;
  }
  * { margin: 0; padding: 0; box-sizing: border-box; }
  html, body {
    width: 937px; height: 1200px; overflow: hidden;
    background: var(--backdrop);
    font-family: "Poppins", sans-serif;
  }
  .card {
    position: absolute; left: 115px; width: 708px; height: 405px;
    background: var(--card-dark);
    box-shadow: 0 4px 18px rgba(0,0,0,0.35);
    overflow: hidden;
  }
  .card--front { top: 140px; }
  .card--back { top: 657px; }

  .brand { position: absolute; text-align: right; color: var(--teal); font-weight: 500; }
  .brand__name { display: block; line-height: 1; letter-spacing: 0.02em; }
  .brand__tagline { display: block; text-transform: uppercase; }
  .brand__licence { display: block; }

  .card--front .brand { right: 144px; top: 58px; }
  .card--front .brand__name { font-size: 124px; }
  .card--front .brand__tagline { font-size: 20px; letter-spacing: 0.2em; margin-top: 4px; }
  .card--front .brand__licence { font-size: 21px; margin-top: 8px; }

  .phone { position: absolute; left: 144px; top: 261px; display: flex; align-items: center; gap: 25px; }
  .phone__icon { width: 53px; height: 53px; }
  .phone__number { color: var(--white); font-size: 62px; font-weight: 500; letter-spacing: 0.01em; line-height: 1; }

  .back-shape { position: absolute; inset: 0; width: 708px; height: 405px; }
  .card--back .brand { right: 51px; top: 166px; }
  .card--back .brand__name { font-size: 62px; }
  .card--back .brand__tagline { font-size: 12.5px; letter-spacing: 0.2em; margin-top: 4px; }
  .card--back .brand__licence { font-size: 13px; margin-top: 4px; }

  .services { position: absolute; left: 32px; top: 0; list-style: none; }
  .service {
    position: absolute; left: 0; display: flex; align-items: center; gap: 16px;
    transform: translateY(-50%); white-space: nowrap;
  }
  .service__icon {
    width: 46px; height: 46px; border-radius: 50%;
    background: var(--icon-fill); border: 2.5px solid var(--ink); flex: none;
  }
  .service__label { color: var(--ink); font-size: 21.5px; font-weight: 500; line-height: 1.18; }
</style>
</head>
<body>

<section class="card card--front">
  <div class="brand">
    <span class="brand__name">K.T.L</span>
    <span class="brand__tagline">Electrical Services P/L</span>
    <span class="brand__licence">EC 20481</span>
  </div>
  <div class="phone">
    <svg class="phone__icon" viewBox="0 0 53 53" aria-hidden="true">
      <circle cx="26.5" cy="26.5" r="26.5" fill="#8fb3b4"/>
      <path d="M18 14 l6 -1 3 8 -4 3 c2 5 5 8 10 10 l3 -4 8 3 -1 6 c-1 2 -3 3 -5 3 C24 41 12 29 12 19 c0 -2 2 -4 6 -5z" fill="#1f2a30"/>
      <path d="M30 14 a10 10 0 0 1 9 9 M30 19 a5 5 0 0 1 4 4" stroke="#1f2a30" stroke-width="2" fill="none" stroke-linecap="round"/>
    </svg>
    <span class="phone__number">0491736250</span>
  </div>
</section>

<section class="card card--back">
  <svg class="back-shape" viewBox="0 0 708 405" aria-hidden="true">
    <rect width="708" height="405" fill="#93b4b5"/>
    <path d="M438 0 C300 110 300 295 428 405 L708 405 L708 0 Z" fill="#ffffff"/>
    <path d="M446 0 C310 112 310 296 436 405 L708 405 L708 0 Z" fill="#8fb3b4"/>
    <path d="M455 0 C318 112 318 298 445 405 L708 405 L708 0 Z" fill="#1f2a30"/>
  </svg>

  <ul class="services">
    <li class="service" style="top:80px">
      <span class="service__icon" role="img" aria-label="Residential and commercial icon"></span>
      <span class="service__label">Residential &amp;<br>Commercial</span>
    </li>
    <li class="service" style="top:159px">
      <span class="service__icon" role="img" aria-label="Maintenance icon"></span>
      <span class="service__label">Maintenance</span>
    </li>
    <li class="service" style="top:238px">
      <span class="service__icon" role="img" aria-label="Solar panel and battery icon"></span>
      <span class="service__label">PV &amp; Battery<br>servicing</span>
    </li>
    <li class="service" style="top:319px">
      <span class="service__icon" role="img" aria-label="EV charger icon"></span>
      <span class="service__label">EV Chargers</span>
    </li>
  </ul>

  <div class="brand">
    <span class="brand__name">K.T.L</span>
    <span class="brand__tagline">Electrical Services P/L</span>
    <span class="brand__licence">EC 20481</span>
  </div>
</section>

</body>
</html>
```